Lantern Care Solutions Banner Ad

Need a 750 x 250-pixel banner ad with the company Logo included. Please see company website at www.lanterncaresolutions.example for more information.

```html
<!DOCTYPE html>
<html lang="en">
<head>
<meta charset="utf-8">
<title>Lantern Care Solutions – Support Coordination Banner</title>
<link rel="stylesheet" href="https://fonts.googleapis.com/css2?family=Poppins:wght@500;600;700;800&display=swap">
<style>
  :root {
    --navy: #0b2a55;
    --navy-deep: #081d3d;
    --navy-light: #1c4f8c;
    --green: #5cb531;
    --green-soft: rgba(116, 196, 66, 0.85);
    --bg-light: #f4f5f7;
    --bg-mid: #e6e8ec;
    --white: #ffffff;
  }
  * { margin: 0; padding: 0; box-sizing: border-box; }
  html, body {
    width: 1200px;
    height: 400px;
    overflow: hidden;
    background: var(--white);
  }
  .banner {
    position: relative;
    width: 1200px;
    height: 400px;
    overflow: hidden;
    font-family: "Poppins", sans-serif;
    background: linear-gradient(90deg, var(--white) 0%, var(--bg-light) 45%, var(--bg-mid) 100%);
  }
  .banner-shapes {
    position: absolute;
    inset: 0;
    width: 1200px;
    height: 400px;
  }
  .photo-area {
    position: absolute;
    inset: 0;
    width: 1200px;
    height: 400px;
  }
  .headline {
    position: absolute;
    left: 82px;
    top: 48px;
    color: var(--navy);
  }
  .headline-intro {
    font-size: 28px;
    font-weight: 600;
    letter-spacing: 1px;
    line-height: 1.2;
  }
  .headline-block {
    position: relative;
    margin-top: 6px;
    padding-left: 4px;
  }
  .headline-accent {
    position: absolute;
    left: -16px;
    top: 12px;
    width: 4px;
    height: 108px;
    background: var(--green);
  }
  .headline-main {
    font-size: 68px;
    font-weight: 800;
    line-height: 1.05;
    letter-spacing: 1px;
    background: linear-gradient(180deg, var(--navy-light) 0%, var(--navy-deep) 100%);
    -webkit-background-clip: text;
    background-clip: text;
    color: transparent;
  }
  .headline-sub {
    font-size: 30px;
    font-weight: 500;
    line-height: 1.2;
    color: var(--navy);
  }
  .brand {
    position: absolute;
    left: 70px;
    top: 296px;
    display: flex;
    align-items: center;
    gap: 12px;
  }
  .brand-mark {
    width: 34px;
    height: 34px;
    border-radius: 50%;
    background: var(--navy);
  }
  .brand-name {
    font-size: 24px;
    font-weight: 700;
    color: var(--green);
    line-height: 1;
  }
</style>
</head>
<body>
  <div class="banner">
    <svg class="banner-shapes" viewBox="0 0 1200 400" aria-hidden="true">
      <polygon points="430,0 560,0 700,200 560,400 430,400 570,200" fill="#ffffff" opacity="0.9"/>
      <polygon points="500,0 610,0 750,200 610,400 500,400 640,200" fill="#dfe3e8" opacity="0.6"/>
    </svg>

    <svg class="photo-area" viewBox="0 0 1200 400" role="img" aria-label="Photo of a smiling young girl in pink top and denim overalls being hugged by a smiling blonde woman">
      <defs>
        <linearGradient id="photoTone" x1="0" y1="0" x2="1" y2="1">
          <stop offset="0" stop-color="#dfe6ea"/>
          <stop offset="0.45" stop-color="#e9c9c4"/>
          <stop offset="0.75" stop-color="#d8b79a"/>
          <stop offset="1" stop-color="#c9d3dc"/>
        </linearGradient>
      </defs>
      <polygon points="610,0 1200,0 1200,400 610,400 750,200" fill="url(#photoTone)"/>
      <polygon points="540,0 610,0 750,200 610,400 540,400 680,200" fill="#74c442" opacity="0.85"/>
      <polygon points="610,0 660,0 800,200 660,400 610,400 750,200" fill="#ffffff" opacity="0.25"/>
      <polygon points="1070,0 1200,0 1200,140" fill="#0b2a55"/>
      <polygon points="1120,0 1200,0 1200,70" fill="#1c4f8c"/>
      <polygon points="1150,400 1200,400 1200,300" fill="#0b2a55" opacity="0.9"/>
    </svg>

    <div class="headline">
      <p class="headline-intro">We serve through</p>
      <div class="headline-block">
        <span class="headline-accent"></span>
        <p class="headline-main">SUPPORT</p>
        <p class="headline-sub">Coordination</p>
      </div>
    </div>

    <div class="brand">
      <span class="brand-mark"></span>
      <span class="brand-name">Lantern Care Solutions</span>
    </div>
  </div>
</body>
</html>
```